Business Card Design

New business card design

Target Market(s)

Residential & Commercial Property Managers

Industry/Entity Type

Plumbing Services

Contact Information for Business Card

Name - Owen Tredgold, title - Director, Phone Number - 0431 862 507, email - owen@rvb-plumbing.com.au, Company ABN - 73 215 904 386,

Font styles to use
Sans Serif

Colors
0054AA
0677BA
7BADD7
CADEEF
E8F1F8

```html
<!DOCTYPE html>
<html lang="en">
<head>
<meta charset="utf-8">
<title>RVB Plumbing Services – Business Card</title>
<link href="https://fonts.googleapis.com/css2?family=Michroma&family=Montserrat:wght@400&display=swap" rel="stylesheet">
<style>
  :root {
    --bg: #e4e7ea;
    --card: #ffffff;
    --card-shade: #eef1f3;
    --ink: #1f2a33;
    --grey: #6f7478;
    --blue: #2ba8e0;
    --blue-deep: #1e98d2;
    --white: #ffffff;
  }
  * { margin: 0; padding: 0; box-sizing: border-box; }
  html, body { width: 1200px; height: 900px; overflow: hidden; background: var(--bg); }
  .canvas { position: relative; width: 1200px; height: 900px; }

  .card {
    position: absolute;
    left: 300px;
    width: 600px;
    height: 366px;
    border-radius: 26px;
    overflow: hidden;
    background: linear-gradient(160deg, var(--card) 55%, var(--card-shade) 100%);
    box-shadow: 0 10px 30px rgba(0,0,0,0.18);
  }
  .card--front { top: 70px; }
  .card--back { top: 470px; }

  .brand { position: absolute; display: flex; align-items: center; gap: 14px; color: var(--ink); font-family: "Montserrat", sans-serif; font-weight: 400; }
  .brand__dot { width: 18px; height: 18px; border-radius: 50%; background: var(--blue); flex: none; }
  .brand__text { display: flex; flex-direction: column; line-height: 1; }
  .brand__name { letter-spacing: 2px; }
  .brand__tag { letter-spacing: 7px; margin-top: 10px; }

  .card--front .brand { left: 50%; top: 50%; transform: translate(-50%, -50%); }
  .card--front .brand__name { font-size: 86px; }
  .card--front .brand__tag { font-size: 13px; }

  .card--back .brand { left: 40px; top: 38px; }
  .card--back .brand__name { font-size: 54px; }
  .card--back .brand__tag { font-size: 10px; letter-spacing: 5px; margin-top: 8px; }
  .card--back .brand__dot { width: 13px; height: 13px; }

  .back-art { position: absolute; inset: 0; }

  .person { position: absolute; left: 40px; top: 182px; font-family: "Michroma", sans-serif; }
  .person__name { color: var(--blue); font-size: 21px; }
  .person__title { color: var(--grey); font-size: 11px; letter-spacing: 1px; margin-top: 6px; }

  .abn { position: absolute; left: 404px; top: 150px; color: var(--white); font-family: "Michroma", sans-serif; font-size: 10px; letter-spacing: 0.5px; }

  .contacts { position: absolute; left: 40px; top: 262px; list-style: none; font-family: "Michroma", sans-serif; color: var(--white); }
  .contacts li { display: flex; align-items: center; gap: 10px; height: 28px; font-size: 15px; }
  .contacts li.contacts__phone { font-size: 18px; }
  .contacts svg { width: 17px; height: 17px; flex: none; }
</style>
</head>
<body>
<main class="canvas">

  <section class="card card--front" aria-label="Business card front">
    <div class="brand">
      <span class="brand__dot"></span>
      <div class="brand__text">
        <span class="brand__name">rvb</span>
        <span class="brand__tag">plumbing services</span>
      </div>
    </div>
  </section>

  <section class="card card--back" aria-label="Business card back">
    <svg class="back-art" viewBox="0 0 600 366" aria-hidden="true">
      <circle cx="560" cy="160" r="190" fill="var(--blue-deep)"/>
      <path d="M420 300 Q520 290 600 180" fill="none" stroke="var(--white)" stroke-width="10" stroke-linecap="round"/>
      <path d="M0 252 H270 L290 208 H600 V366 H0 Z" fill="var(--blue)"/>
    </svg>

    <div class="brand">
      <span class="brand__dot"></span>
      <div class="brand__text">
        <span class="brand__name">rvb</span>
        <span class="brand__tag">plumbing services</span>
      </div>
    </div>

    <p class="abn">ABN 73 215 904 386</p>

    <div class="person">
      <p class="person__name">Owen Tredgold</p>
      <p class="person__title">DIRECTOR</p>
    </div>

    <ul class="contacts">
      <li class="contacts__phone">
        <svg viewBox="0 0 20 20" fill="none" stroke="currentColor" stroke-width="1.5"><rect x="1" y="1" width="18" height="18" rx="5"/><path d="M6 7c0 4 3 7 7 7l1-2-2-1-1 1c-1-.5-2.5-2-3-3l1-1-1-2z" fill="currentColor" stroke="none"/></svg>
        0431 862 507
      </li>
      <li>
        <svg viewBox="0 0 20 20" fill="none" stroke="currentColor" stroke-width="1.5"><rect x="1" y="1" width="18" height="18" rx="5"/><rect x="5" y="6.5" width="10" height="7" fill="currentColor" stroke="none"/><path d="M5 6.5l5 4 5-4" stroke="var(--blue)" stroke-width="1"/></svg>
        owen@rvb-plumbing.com.au
      </li>
      <li>
        <svg viewBox="0 0 20 20" fill="none" stroke="currentColor" stroke-width="1.5"><rect x="1" y="1" width="18" height="18" rx="5"/><circle cx="10" cy="10" r="5" stroke-width="1.2"/><path d="M5 10h10M10 5c-2.5 3-2.5 7 0 10M10 5c2.5 3 2.5 7 0 10" stroke-width="1"/></svg>
        www.rvb-plumbing.com.au
      </li>
    </ul>
  </section>

</main>
</body>
</html>
```